14 years in business and its time for a new look and feel brochure and business cards!

We are looking to create a brochure that is professional and eye catching to bring in new commercial business. After14 years in business we have finally redone our logo and it is time to get a brochure completed as well. The logo that should be used is the one that says Inc. We want this new brochure to appeal to corporate property management companies and smaller apartment complexes. We want it to look rich and have the same high quality our work has.

Target Market(s)

property management companies and apartment complexes in the DMV.

Industry/Entity Type

Construction Company

Contact Information for Business Card

Logo
Dovid Rennick
CEO
Mobile 410-555-0137
Office 410-555-0192
Address 3817 Larchmont Lane Suite B Baltimore, MD 21208
Email DR@BrightCoatInc.example

Font styles to use
Sans Serif

Requirements
Must have
• Want the background to be black and silver gradient. Will be printing on high gloss and would like for it to be rich looking.
• brochure will be 8.5x11. open minded in terms of the fold, how it looks best with the design provided will determine that. Can be bi-fold, try-fold or z-fold.
• Content for brochure:About us
• Founded in 2003, The Bright Coat Inc. was the vision of Dovid Rennick, with a commitment to becoming the premier renovator and developer of residential and commercial properties in the DMV. Today, The Bright Coat Inc. is widely respected for their gold standard in quality and efficiency and continues to grow by attracting the highest level of professionals with knowledge and experience in our field.
• The Bright Coat Inc.’s most valuable asset is our team members. The efforts they put forth are the key to meeting our standards and providing all of our valued clients with the highest quality of service. Leading our wonderful team members is a group of management like no other. With years of experience, the power to motivate and the keen eye to ensure top quality, our team of experts focus all of their energy to exceed our client’s expectations.
• Our Mission
• We strive to provide timely delivery, the highest level of quality and value on every project. We offer unsurpassed dedication to maintain our working relationships and consistently deliver the best service to ensure our clients success.
• Property Renovations
• The Bright Coat Inc. has been responsible for coordinating the construction and renovation of many projects, including all parts of a building’s interior and exterior. Well known for attention to details, quality and timely execution, The Bright Coat Inc. has managed and executed more than 4,000 turnovers and over 150 projects in the last 3 years alone.
• Renovations not only improve the appeal and marketability of your property, but also add value. Interior and exterior renovations help make any property more functional, energy-efficient and enable you to keep up with what your market demands. From the smallest change of a door knob to a complete kitchen overhaul, these are the things that make all the difference in your property. We are committed to deliver great value, and we do that by ensuring that our experts are involved in the renovation process, providing input and quality maintenance throughout the entire renovation.
• Services Include
• Painting
• Flooring
• Sub-Flooring
• Crown molding
• Siding & Wood Replacement
• Trim & Carpentry Work
• Punches
• Decks
• Power wash
• Concrete & Paving
• Turnovers including plumbing and electric
• Kitchen overhauls
• We offer first time clients a free apartment paint or punch on us to show you the quality you can always expect!
• Call today to schedule your first-time paint or punch at 410-555-0192.

```html
<!DOCTYPE html>
<html lang="en">
<head>
<meta charset="utf-8">
<title>The Bright Coat Inc. – Brochure and Business Cards</title>
<link rel="stylesheet" href="https://fonts.googleapis.com/css2?family=Michroma&family=Lato:wght@400;700&display=swap">
<style>
  :root{
    --page:#ffffff;
    --black:#0e0e0e;
    --charcoal:#262626;
    --graphite:#3a3a3a;
    --silver:#cfcfcf;
    --silver-dark:#8d8d8d;
    --ink:#f1f1f1;
    --muted:#d6d6d6;
    --head-font:"Michroma", sans-serif;
    --body-font:"Lato", sans-serif;
  }
  *{box-sizing:border-box;margin:0;padding:0}
  html,body{width:1200px;height:1200px;overflow:hidden;background:var(--page)}
  body{position:relative;font-family:var(--body-font);color:var(--ink)}

  .sheet{position:absolute;overflow:hidden;
    background:linear-gradient(180deg,#2c2c2c 0%,var(--black) 45%,#1c1c1c 100%);
    box-shadow:0 2px 6px rgba(0,0,0,.35)}
  .brochure-outside{left:32px;top:34px;width:720px;height:558px}
  .brochure-inside{left:32px;top:610px;width:720px;height:558px}
  .card-front{left:770px;top:613px;width:412px;height:240px}
  .card-back{left:770px;top:873px;width:412px;height:240px}

  .art{position:absolute;inset:0;width:100%;height:100%}
  .panel-fold{position:absolute;top:0;bottom:0;width:1px;background:rgba(255,255,255,.04)}

  .heading{font-family:var(--head-font);font-size:9.5px;letter-spacing:.4px;color:var(--ink);text-transform:uppercase}
  .copy{font-size:6.9px;line-height:9.6px;text-align:justify;color:var(--muted)}

  /* outside, left panel */
  .about{position:absolute;left:26px;top:250px;width:194px}
  .about .heading{margin-bottom:14px}
  .about .copy{margin-bottom:10px}
  .about .mission{margin-top:14px}

  /* outside, centre panel */
  .offer{position:absolute;left:250px;width:212px;top:92px;text-align:center}
  .offer .big{font-family:var(--head-font);font-size:13px;color:var(--silver);line-height:17px}
  .offer .mid{font-family:var(--head-font);font-size:10px;color:var(--silver);line-height:16px}
  .offer .line{font-size:12px;line-height:16px;color:var(--ink)}
  .offer .small{font-size:9.5px;letter-spacing:.2px;color:var(--silver);line-height:15px}
  .offer-rule{position:absolute;left:260px;top:212px;width:196px;height:1px;background:var(--graphite)}
  .call{position:absolute;left:250px;width:212px;top:231px;text-align:center}
  .phone-line{display:flex;align-items:center;justify-content:center;gap:6px;margin-top:10px;
    font-family:var(--head-font);font-size:12.5px;color:var(--ink)}
  .wordmark{font-family:var(--head-font);color:var(--ink);text-align:center;display:flex;align-items:center;justify-content:center;gap:6px}
  .wordmark .dot{width:14px;height:14px;border-radius:50%;background:var(--silver);flex:none}
  .centre-mark{position:absolute;left:250px;width:212px;top:400px;font-size:10.5px}
  .contact-stack{position:absolute;left:250px;width:212px;top:446px;text-align:center;font-size:6.9px;font-weight:700;color:var(--ink)}
  .contact-stack .item{display:flex;flex-direction:column;align-items:center;gap:2px;margin-bottom:8px}

  /* outside, right panel */
  .cover-mark{position:absolute;left:490px;width:210px;top:70px;font-size:13px;flex-direction:column;gap:8px}
  .cover-mark .dot{width:30px;height:30px}
  .tagline{position:absolute;left:490px;width:230px;top:468px;text-align:center;color:var(--black);font-family:var(--head-font)}
  .tagline .t1{font-size:18px;line-height:22px}
  .tagline .t2{font-size:13px;line-height:18px}
  .cover-url{position:absolute;left:500px;width:220px;top:528px;text-align:center;font-size:7px;letter-spacing:3px;color:var(--muted)}

  /* inside */
  .renovations{position:absolute;left:26px;top:26px;width:194px}
  .renovations .heading{margin-bottom:14px}
  .renovations .copy{margin-bottom:12px}
  .services-title{position:absolute;left:250px;width:212px;top:26px;text-align:center}
  .services-rule{position:absolute;left:258px;top:44px;width:196px;height:1px;background:var(--graphite)}
  .service{position:absolute;width:110px;margin-left:-55px;text-align:center;font-size:8px;line-height:11px;color:var(--muted)}
  .service svg{display:block;margin:0 auto 4px;width:26px;height:26px}

  /* cards */
  .card-name{position:absolute;right:22px;top:22px;text-align:right}
  .card-name .name{font-family:var(--head-font);font-size:9.5px;color:var(--ink)}
  .card-name .role{font-size:10px;color:var(--muted);margin-top:2px}
  .card-contacts{position:absolute;right:22px;top:70px;text-align:right;font-size:8.4px;color:var(--muted)}
  .card-contacts .row{display:flex;justify-content:flex-end;align-items:center;gap:8px;height:20px}
  .card-contacts .row svg{width:12px;height:12px;flex:none}
  .card-contacts .address{line-height:11px;height:30px}
  .card-mark{position:absolute;left:20px;top:88px;width:176px;font-size:11.5px;flex-direction:column;gap:8px}
  .card-mark .dot{width:34px;height:34px}
  .back-mark{position:absolute;left:0;right:0;top:66px;font-size:16px;flex-direction:column;gap:10px}
  .back-mark .dot{width:40px;height:40px}
  .back-url{position:absolute;left:0;right:0;top:206px;text-align:center;font-size:8.5px;letter-spacing:2.6px;color:var(--muted)}
</style>
</head>
<body>

<!-- Brochure, outside spread -->
<section class="sheet brochure-outside" aria-label="Brochure outside spread">
  <svg class="art" viewBox="0 0 720 558" aria-hidden="false">
    <defs>
      <linearGradient id="silverBand" x1="0" y1="0" x2="0" y2="1">
        <stop offset="0" stop-color="#f2f2f2"/><stop offset="1" stop-color="#a9a9a9"/>
      </linearGradient>
      <linearGradient id="roomTones" x1="0" y1="0" x2="1" y2="1">
        <stop offset="0" stop-color="#d8d3c4"/><stop offset=".6" stop-color="#8c8a7c"/><stop offset="1" stop-color="#6e5e4b"/>
      </linearGradient>
      <linearGradient id="kitchenTones" x1="0" y1="0" x2="0" y2="1">
        <stop offset="0" stop-color="#d9d6cf"/><stop offset=".45" stop-color="#efeeea"/><stop offset=".7" stop-color="#6a6866"/><stop offset="1" stop-color="#b9b6b0"/>
      </linearGradient>
    </defs>
    <path d="M262 0 Q226 178 0 218 V232 Q240 196 282 0 Z" fill="#5a5a5a"/>
    <path d="M0 0 H262 Q222 170 0 212 Z" fill="url(#roomTones)" role="img" aria-label="Photo of a freshly painted empty basement room with carpet"/>
    <path d="M720 128 Q500 150 438 330 L430 462 H452 V330 Q520 160 720 138 Z" fill="#7a7a7a"/>
    <path d="M720 138 Q520 160 452 330 V462 H720 Z" fill="url(#kitchenTones)" role="img" aria-label="Photo of a renovated white kitchen with tiled backsplash and steel appliances"/>
    <path d="M452 462 H720 V518 H476 Q462 490 452 462 Z" fill="url(#silverBand)"/>
    <path d="M476 518 H720 V558 H496 Z" fill="#4b4b4b"/>
    <path d="M430 462 Q440 520 500 558 H490 Q430 520 420 462 Z" fill="#9a9a9a"/>
    <rect x="240" y="0" width="1" height="558" fill="#ffffff" opacity=".04"/>
    <rect x="480" y="0" width="1" height="558" fill="#ffffff" opacity=".04"/>
  </svg>

  <div class="about">
    <h2 class="heading">About Us</h2>
    <p class="copy">Founded in 2003, The Bright Coat Inc. was the vision of Dovid Rennick, with a commitment to becoming the premier renovator and developer of residential and commercial properties in the DMV. Today, The Bright Coat Inc. is widely respected for their gold standard in quality and efficiency and continues to grow by attracting the highest level of professionals with knowledge and experience in our field.</p>
    <p class="copy">The Bright Coat Inc.’s most valuable asset is our team members. The efforts they put forth are the key to meeting our standards and providing all of our valued clients with the highest quality of service. Leading our wonderful team members is a group of management like no other. With years of experience, the power to motivate and the keen eye to ensure top quality, our team of experts focus all of their energy to exceed our client’s expectations.</p>
    <h2 class="heading mission">Our Mission</h2>
    <p class="copy" style="margin-top:12px">We strive to provide timely delivery, the highest level of quality and value on every project. We offer unsurpassed dedication to maintain our working relationships and consistently deliver the best service to ensure our clients success.</p>
  </div>

  <div class="offer">
    <div class="big">WE OFFER</div>
    <div class="line">first time clients a</div>
    <div class="mid">FREE APARTMENT</div>
    <div class="line">paint or punch on us</div>
    <div class="small">TO SHOW YOU THE QUALITY</div>
    <div class="line">you can always expect!</div>
  </div>
  <div class="offer-rule"></div>
  <div class="call offer">
    <div class="big">CALL TODAY</div>
    <div class="line">to schedule your</div>
    <div class="mid">FIRST-TIME</div>
    <div class="line">paint or punch at</div>
    <div class="phone-line">
      <svg width="14" height="14" viewBox="0 0 24 24" aria-hidden="true"><path d="M6 2h4l2 5-2.5 1.5a11 11 0 0 0 6 6L17 12l5 2v4a2 2 0 0 1-2 2A18 18 0 0 1 4 4a2 2 0 0 1 2-2z" fill="#f1f1f1"/></svg>
      <span>410-555-0192</span>
    </div>
  </div>

  <div class="wordmark centre-mark"><span class="dot"></span><span>THE BRIGHT COAT INC</span></div>

  <div class="contact-stack">
    <div class="item">
      <svg width="12" height="10" viewBox="0 0 24 18" aria-hidden="true"><rect x="1" y="1" width="22" height="16" fill="#f1f1f1"/><path d="M1 1l11 9 11-9" stroke="#111" stroke-width="2" fill="none"/></svg>
      <span>dr@brightcoatinc.example</span>
    </div>
    <div class="item">
      <svg width="12" height="12" viewBox="0 0 24 24" aria-hidden="true"><circle cx="12" cy="12" r="10" fill="none" stroke="#f1f1f1" stroke-width="2"/><path d="M2 12h20M12 2c4 4 4 16 0 20M12 2c-4 4-4 16 0 20" stroke="#f1f1f1" stroke-width="1.6" fill="none"/></svg>
      <span>www.brightcoatinc.example</span>
    </div>
    <div class="item">
      <svg width="13" height="12" viewBox="0 0 24 22" aria-hidden="true"><path d="M12 1L1 11h3v10h6v-6h4v6h6V11h3z" fill="#f1f1f1"/></svg>
      <span>3817 Larchmont Lane, Suite B, Baltimore, MD 21208</span>
    </div>
  </div>

  <div class="wordmark cover-mark"><span class="dot"></span><span>THE BRIGHT COAT INC</span></div>
  <div class="tagline"><div class="t1">A STEP</div><div class="t2">Above The Rest</div></div>
  <div class="cover-url">www.brightcoatinc.example</div>
</section>

<!-- Brochure, inside spread -->
<section class="sheet brochure-inside" aria-label="Brochure inside spread">
  <svg class="art" viewBox="0 0 720 558">
    <defs>
      <linearGradient id="woodKitchen" x1="0" y1="0" x2="1" y2="1">
        <stop offset="0" stop-color="#e9d9a8"/><stop offset=".5" stop-color="#4a2a22"/><stop offset="1" stop-color="#2b1a16"/>
      </linearGradient>
      <linearGradient id="deckTones" x1="0" y1="0" x2="0" y2="1">
        <stop offset="0" stop-color="#a24c3c"/><stop offset=".35" stop-color="#d6cbb4"/><stop offset=".7" stop-color="#8a4a3a"/><stop offset="1" stop-color="#3a2a24"/>
      </linearGradient>
    </defs>
    <path d="M0 284 Q170 260 310 340 L300 350 Q170 276 0 300 Z" fill="#8a8a8a"/>
    <path d="M0 300 Q170 276 300 350 L300 558 H0 Z" fill="url(#woodKitchen)" role="img" aria-label="Photo of a renovated kitchen with dark wood cabinets"/>
    <path d="M270 558 Q280 400 460 326 Q600 266 720 254 V262 Q600 274 470 334 Q300 410 290 558 Z" fill="#9c9c9c"/>
    <path d="M290 558 Q300 410 470 334 Q600 274 720 262 V558 Z" fill="url(#deckTones)" role="img" aria-label="Photo of a new wooden deck on a brick building"/>
    <rect x="240" y="0" width="1" height="558" fill="#ffffff" opacity=".04"/>
    <rect x="480" y="0" width="1" height="558" fill="#ffffff" opacity=".04"/>
  </svg>

  <div class="renovations">
    <h2 class="heading">Property Renovations</h2>
    <p class="copy">The Bright Coat Inc. has been responsible for coordinating the construction and renovation of many projects, including all parts of a building’s interior and exterior. Well known for attention to details, quality and timely execution, The Bright Coat Inc. has managed and executed more than 4,000 turnovers and over 150 projects in the last 3 years alone.</p>
    <p class="copy">Renovations not only improve the appeal and marketability of your property, but also add value. Interior and exterior renovations help make any property more functional, energy-efficient and enable you to keep up with what your market demands. From the smallest change of a door knob to a complete kitchen overhaul, these are the things that make all the difference in your property. We are committed to deliver great value, and we do that by ensuring that our experts are involved in the renovation process, providing input and quality maintenance throughout the entire renovation.</p>
  </div>

  <h2 class="heading services-title">Services Include</h2>
  <div class="services-rule"></div>

  <div class="service" style="left:296px;top:72px"><svg viewBox="0 0 24 24"><rect x="4" y="2" width="14" height="7" rx="1" fill="none" stroke="#f1f1f1" stroke-width="2"/><path d="M18 5h3v7h-9v3" fill="none" stroke="#f1f1f1" stroke-width="2"/><rect x="10" y="15" width="4" height="8" fill="#f1f1f1"/></svg>Painting</div>
  <div class="service" style="left:410px;top:72px"><svg viewBox="0 0 24 24"><rect x="2" y="17" width="20" height="5" fill="#f1f1f1"/><path d="M5 17l4-8h6l4 8" fill="none" stroke="#f1f1f1" stroke-width="2"/></svg>Flooring</div>
  <div class="service" style="left:540px;top:14px"><svg viewBox="0 0 24 24"><rect x="3" y="5" width="12" height="6" fill="#f1f1f1"/><path d="M15 8h7M7 11v10" stroke="#f1f1f1" stroke-width="2.5"/></svg>Punches</div>
  <div class="service" style="left:654px;top:14px"><svg viewBox="0 0 24 24"><rect x="2" y="4" width="20" height="16" fill="none" stroke="#f1f1f1" stroke-width="2"/><path d="M6 20L12 4M11 20L17 4M16 20l4-10" stroke="#f1f1f1" stroke-width="1.5"/></svg>Decks</div>
  <div class="service" style="left:296px;top:152px"><svg viewBox="0 0 24 24"><path d="M2 16l14-8 6 4-14 8z" fill="none" stroke="#f1f1f1" stroke-width="2"/><path d="M5 15l12-7" stroke="#f1f1f1" stroke-width="1"/></svg>Sub-Flooring</div>
  <div class="service" style="left:410px;top:152px"><svg viewBox="0 0 24 24"><path d="M5 3c3 2 4 6 8 9s4 6 6 9" fill="none" stroke="#f1f1f1" stroke-width="3"/></svg>Crown molding</div>
  <div class="service" style="left:540px;top:92px"><svg viewBox="0 0 24 24"><rect x="7" y="9" width="10" height="14" rx="2" fill="none" stroke="#f1f1f1" stroke-width="2"/><path d="M9 9V4h6l3 2M4 4h2M3 7h2" stroke="#f1f1f1" stroke-width="2" fill="none"/></svg>Power wash</div>
  <div class="service" style="left:654px;top:92px"><svg viewBox="0 0 24 24"><path d="M4 12a8 8 0 0 1 16 0v8H4z" fill="none" stroke="#f1f1f1" stroke-width="2"/><circle cx="7" cy="20" r="2" fill="#f1f1f1"/><circle cx="17" cy="20" r="2" fill="#f1f1f1"/></svg>Concrete &amp; Paving</div>
  <div class="service" style="left:296px;top:242px"><svg viewBox="0 0 24 24"><rect x="3" y="3" width="18" height="18" fill="none" stroke="#f1f1f1" stroke-width="2"/><path d="M6 18L18 6M6 13l7-7M11 18l7-7" stroke="#f1f1f1" stroke-width="1.5"/></svg>Siding &amp; Wood<br>Replacement</div>
  <div class="service" style="left:410px;top:242px"><svg viewBox="0 0 24 24"><path d="M4 20L18 6M6 4l14 14" stroke="#f1f1f1" stroke-width="2.5"/><rect x="15" y="2" width="7" height="5" fill="#f1f1f1"/></svg>Trim &amp; Carpentry<br>Work</div>
  <div class="service" style="left:540px;top:182px"><svg viewBox="0 0 24 24"><path d="M8 3h4v8h8v4H12v6H8v-6H2v-4h6z" fill="none" stroke="#f1f1f1" stroke-width="2"/></svg>Turnovers including<br>plumbing and electric</div>
  <div class="service" style="left:654px;top:182px"><svg viewBox="0 0 24 24"><rect x="3" y="3" width="18" height="18" fill="none" stroke="#f1f1f1" stroke-width="2"/><path d="M3 9h18M7 13h10M7 17h10" stroke="#f1f1f1" stroke-width="1.5"/></svg>Kitchen overhauls</div>
</section>

<!-- Business card, front -->
<section class="sheet card-front" aria-label="Business card front">
  <svg class="art" viewBox="0 0 412 240">
    <path d="M0 0 H412 V2 Q200 0 0 22 Z" fill="#3c3c3c"/>
    <path d="M0 20 Q150 4 260 0 H300 Q140 8 0 26 Z" fill="#d2d2d2"/>
    <path d="M0 240 V218 Q180 176 412 200 V206 Q200 190 0 234 Z" fill="#d8d8d8"/>
    <path d="M0 240 V234 Q200 190 412 206 V240 Z" fill="#161616"/>
  </svg>
  <div class="card-name"><div class="name">Dovid Rennick</div><div class="role">CEO</div></div>
  <div class="card-contacts">
    <div class="row"><span>410-555-0137</span><svg viewBox="0 0 24 24"><rect x="7" y="2" width="10" height="20" rx="2" fill="none" stroke="#f1f1f1" stroke-width="2"/><circle cx="12" cy="18" r="1.3" fill="#f1f1f1"/></svg></div>
    <div class="row"><span>410-555-0192</span><svg viewBox="0 0 24 24"><path d="M2 8c6-5 14-5 20 0l-3 3-3-2V7H8v2l-3 2z" fill="#f1f1f1"/><rect x="5" y="13" width="14" height="8" rx="1" fill="#f1f1f1"/></svg></div>
    <div class="row"><span>dr@brightcoatinc.example</span><svg viewBox="0 0 24 18"><rect x="1" y="1" width="22" height="16" fill="#f1f1f1"/><path d="M1 1l11 9 11-9" stroke="#111" stroke-width="2" fill="none"/></svg></div>
    <div class="row"><span>www.brightcoatinc.example</span><svg viewBox="0 0 24 24"><circle cx="12" cy="12" r="10" fill="none" stroke="#f1f1f1" stroke-width="2"/><path d="M2 12h20M12 2c4 4 4 16 0 20M12 2c-4 4-4 16 0 20" stroke="#f1f1f1" stroke-width="1.6" fill="none"/></svg></div>
    <div class="row address"><span>3817 Larchmont Lane,<br>Suite B, Baltimore, MD 21208</span><svg viewBox="0 0 24 22"><path d="M12 1L1 11h3v10h6v-6h4v6h6V11h3z" fill="#f1f1f1"/></svg></div>
  </div>
  <div class="wordmark card-mark"><span class="dot"></span><span>THE BRIGHT COAT INC</span></div>
</section>

<!-- Business card, back -->
<section class="sheet card-back" aria-label="Business card back">
  <div class="wordmark back-mark"><span class="dot"></span><span>THE BRIGHT COAT INC</span></div>
  <div class="back-url">www.brightcoatinc.example</div>
</section>

</body>
</html>
```